Brackenridge Strength Studio Chronic Pain Flyer

Double sided DL flyer required to promote a strength training studio to sufferers of chronic pain. Flyer will be displayed in osteopathy, chiropractic and massage clinics. Flyer should be clean, professional and appeal to an older (40+) demographic.

Target Market(s)

Chronic pain sufferers. Age 40+

Industry/Entity Type

Health And Wellness

Colors

Designer to choose colors to be used in the design.

Requirements
Must have
• See attached files for text copy and logo. Image(s) of people strength training with a coach or personal trainer, as well as images depicting pain in common parts of the body (such as those pictured in the supplied mock up)
• website address: brackenridgestrengthstudio.example.com.au
• phone number : 0452 918 304
• Street address: 4/63 Juniper Hollow Rd, Brackenridge
Nice to have
• Images such as in the attached files.

```html
<!DOCTYPE html>
<html lang="en">
<head>
<meta charset="utf-8">
<title>Brackenridge Strength Studio – Chronic Pain Flyer</title>
<link rel="stylesheet" href="https://fonts.googleapis.com/css2?family=Open+Sans:wght@400;600;700;800&family=Roboto+Condensed:wght@700&display=swap">
<style>
  :root {
    --red: #e31b23;
    --red-deep: #b3141b;
    --hero-top: #7a0e12;
    --hero-bottom: #5a0b0e;
    --charcoal: #2b2b2d;
    --ink: #3a3a3a;
    --white: #ffffff;
    --backdrop: #a9a9a9;
    --photo-light: #ececec;
    --photo-mid: #bdbdbd;
  }
  * { box-sizing: border-box; margin: 0; padding: 0; }
  html, body { width: 1200px; height: 1200px; overflow: hidden; }
  body {
    background: var(--backdrop);
    font-family: "Open Sans", Arial, sans-serif;
    position: relative;
  }
  .flyer {
    position: absolute;
    top: 110px;
    width: 490px;
    height: 979px;
    background: var(--white);
    overflow: hidden;
  }
  .flyer--front { left: 82px; }
  .flyer--back { left: 634px; }

  .brand {
    position: absolute;
    top: 58px; left: 0; width: 100%;
    text-align: center;
    color: var(--ink);
    font-weight: 800;
    text-transform: uppercase;
    line-height: 1.05;
  }
  .brand__name { font-size: 30px; letter-spacing: 1px; display: block; }
  .brand__sub { font-size: 19px; letter-spacing: 3px; display: block; }

  .photo { position: absolute; left: 0; width: 100%; }
  .photo--back-pain {
    top: 162px; height: 330px;
    background: linear-gradient(180deg, var(--photo-mid), var(--photo-light));
  }
  .photo--knee-pain {
    top: 423px; height: 328px;
    background: linear-gradient(180deg, var(--photo-light), var(--photo-mid));
  }
  .swoosh { position: absolute; left: 0; width: 490px; }

  .front-title {
    position: absolute; top: 512px; left: 0; width: 100%;
    text-align: center;
    color: var(--red-deep);
    font-weight: 800;
    font-size: 62px;
    line-height: 68px;
    text-transform: uppercase;
  }
  .front-copy {
    position: absolute; top: 720px; left: 36px; right: 36px;
    text-align: center;
    font-size: 14px; line-height: 19.5px;
    color: var(--ink);
  }
  .contact {
    position: absolute; left: 0; width: 100%;
    display: flex; flex-direction: column; align-items: center;
  }
  .front-contact { top: 828px; }
  .back-contact { top: 830px; }
  .contact__row { display: flex; align-items: center; gap: 14px; }
  .contact__phone {
    font-family: "Roboto Condensed", "Arial Narrow", sans-serif;
    font-weight: 700; font-size: 52px; line-height: 58px;
    color: var(--red);
  }
  .contact__address { font-size: 20px; line-height: 30px; }
  .front-contact .contact__address { color: var(--ink); }
  .back-contact .contact__address { color: var(--white); }
  .icon { width: 28px; height: 28px; flex: none; }
  .icon--pin { width: 24px; height: 24px; }

  .footer {
    position: absolute; bottom: 0; left: 0; width: 100%; height: 50px;
    background: var(--red);
    display: flex; align-items: center; justify-content: center; gap: 8px;
    color: var(--white); font-weight: 700; font-size: 13.5px;
  }

  .hero-panel {
    position: absolute; top: 166px; left: 0; width: 100%; height: 257px;
    background: linear-gradient(180deg, var(--hero-top), var(--hero-bottom));
    color: var(--white);
  }
  .hero-panel__kicker {
    position: absolute; top: 26px; left: 60px;
    font-weight: 700; font-size: 39px; line-height: 44px; letter-spacing: .5px;
  }
  .hero-panel__title {
    position: absolute; top: 64px; left: 58px;
    font-weight: 800; font-size: 67px; line-height: 76px;
  }
  .hero-panel__tagline {
    position: absolute; top: 138px; left: 62px;
    font-size: 27px; line-height: 34px;
  }
  .hero-panel__copy {
    position: absolute; top: 176px; left: 50px; right: 50px;
    text-align: center; font-size: 12.5px; line-height: 17px;
  }
  .info-panel {
    position: absolute; top: 751px; left: 0; width: 100%; height: 179px;
    background: var(--charcoal);
  }
  .info-panel__copy {
    position: absolute; top: 20px; left: 40px; right: 40px;
    text-align: center; color: var(--white);
    font-size: 12.5px; line-height: 17px;
  }
</style>
</head>
<body>

<section class="flyer flyer--front">
  <div class="photo photo--back-pain" role="img" aria-label="Photo of a person holding their sore lower back"></div>
  <svg class="swoosh" style="top:0" width="490" height="220" viewBox="0 0 490 220" aria-hidden="true">
    <path d="M0,150 Q260,205 490,98 V0 H0 Z" fill="var(--white)"/>
    <path d="M0,120 Q260,190 490,98 Q270,215 0,178 Z" fill="var(--red)"/>
    <path d="M0,182 Q270,222 490,100 Q270,228 0,190 Z" fill="#cfcfcf"/>
  </svg>
  <svg class="swoosh" style="top:440px" width="490" height="140" viewBox="0 0 490 140" aria-hidden="true">
    <path d="M0,140 Q200,10 490,50 V140 Z" fill="var(--white)"/>
    <path d="M0,118 Q190,-10 490,36 V52 Q230,18 0,135 Z" fill="var(--red)"/>
    <path d="M0,110 Q190,-22 490,28 V34 Q190,-14 0,116 Z" fill="#d6d6d6"/>
  </svg>

  <div class="brand">
    <span class="brand__name">Brackenridge</span>
    <span class="brand__sub">Strength Studio</span>
  </div>

  <h1 class="front-title">Health<br>Through<br>Strength</h1>
  <p class="front-copy">BSS is a boutique personal training facility providing an exceptional level of service to our dedicated clients. BSS is NOT a gym but a private training studio, committed to providing a welcoming and non-judgemental place to train for people looking to get real results.</p>

  <div class="contact front-contact">
    <div class="contact__row">
      <svg class="icon" viewBox="0 0 24 24" aria-hidden="true"><path d="M6.6 2.5l3 3.2-1.8 2.4c.9 2.4 3 4.6 5.6 5.8l2.3-1.8 3.3 3-1.6 3.3c-7.3-.6-13-6.6-13.5-13.7z" fill="none" stroke="var(--ink)" stroke-width="1.8" stroke-linejoin="round"/><path d="M15 3.5a6 6 0 0 1 5.5 5.5M14.5 6.5a3 3 0 0 1 3 3" fill="none" stroke="var(--ink)" stroke-width="1.6" stroke-linecap="round"/></svg>
      <span class="contact__phone">0452 918 304</span>
    </div>
    <div class="contact__row">
      <svg class="icon icon--pin" viewBox="0 0 24 24" aria-hidden="true"><circle cx="12" cy="12" r="11" fill="none" stroke="var(--ink)" stroke-width="1.2"/><path d="M12 18s-4.5-4.6-4.5-7.6a4.5 4.5 0 0 1 9 0C16.5 13.4 12 18 12 18z" fill="var(--red)"/><circle cx="12" cy="10.4" r="1.6" fill="var(--white)"/></svg>
      <span class="contact__address">4/63 Juniper Hollow Rd, Brackenridge</span>
    </div>
  </div>

  <div class="footer">
    <svg class="icon" style="width:20px;height:20px" viewBox="0 0 24 24" aria-hidden="true"><g fill="none" stroke="var(--white)" stroke-width="1.5"><circle cx="12" cy="12" r="10"/><circle cx="12" cy="12" r="6.5"/><ellipse cx="12" cy="12" rx="3" ry="6.5"/><path d="M5.5 12h13M12 5.5v13"/></g></svg>
    <span>brackenridgestrengthstudio.example.com.au</span>
  </div>
</section>

<section class="flyer flyer--back">
  <div class="brand">
    <span class="brand__name">Brackenridge</span>
    <span class="brand__sub">Strength Studio</span>
  </div>

  <div class="hero-panel" role="img" aria-label="Red-tinted photo of a barbell lift in a training studio">
    <div class="hero-panel__kicker">HEALTH THROUGH</div>
    <div class="hero-panel__title">STRENGTH</div>
    <div class="hero-panel__tagline">You don’t have to live in pain</div>
    <p class="hero-panel__copy">Strength training has been shown to improve many chronic pain conditions and is now being routinely recommended by medical and health professionals.</p>
  </div>

  <div class="photo photo--knee-pain" role="img" aria-label="Photo of hands holding a sore knee"></div>

  <div class="info-panel">
    <p class="info-panel__copy">Our private studio provides high quality strength training by expert strength coaches. We’ve helped countless people improve or eliminate chronic pain, contact us today and find out how we can help you.</p>
  </div>

  <div class="contact back-contact">
    <div class="contact__row">
      <svg class="icon" viewBox="0 0 24 24" aria-hidden="true"><path d="M6.6 2.5l3 3.2-1.8 2.4c.9 2.4 3 4.6 5.6 5.8l2.3-1.8 3.3 3-1.6 3.3c-7.3-.6-13-6.6-13.5-13.7z" fill="none" stroke="var(--white)" stroke-width="1.8" stroke-linejoin="round"/><path d="M15 3.5a6 6 0 0 1 5.5 5.5M14.5 6.5a3 3 0 0 1 3 3" fill="none" stroke="var(--white)" stroke-width="1.6" stroke-linecap="round"/></svg>
      <span class="contact__phone">0452 918 304</span>
    </div>
    <div class="contact__row">
      <svg class="icon icon--pin" viewBox="0 0 24 24" aria-hidden="true"><circle cx="12" cy="12" r="11" fill="none" stroke="var(--white)" stroke-width="1.2"/><path d="M12 18s-4.5-4.6-4.5-7.6a4.5 4.5 0 0 1 9 0C16.5 13.4 12 18 12 18z" fill="var(--red)"/><circle cx="12" cy="10.4" r="1.6" fill="var(--white)"/></svg>
      <span class="contact__address">4/63 Juniper Hollow Rd, Brackenridge</span>
    </div>
  </div>

  <div class="footer">
    <svg class="icon" style="width:20px;height:20px" viewBox="0 0 24 24" aria-hidden="true"><g fill="none" stroke="var(--white)" stroke-width="1.5"><circle cx="12" cy="12" r="10"/><circle cx="12" cy="12" r="6.5"/><ellipse cx="12" cy="12" rx="3" ry="6.5"/><path d="M5.5 12h13M12 5.5v13"/></g></svg>
    <span>brackenridgestrengthstudio.example.com.au</span>
  </div>
</section>

</body>
</html>
```